Flyer-Design für Lindauer Hotel
Zielgruppe
Lindauer Hotel
Aufgabenstellung
Texte: siehe alten Fyler,
drei Sterne dürfen nicht mehr in den Texten auftauchen.
www.lindauer-hotel-beispiel.de

```html
<!DOCTYPE html>
<html lang="de">
<head>
<meta charset="utf-8">
<title>Lindauer Hotel – Flyer</title>
<link rel="stylesheet" href="https://fonts.googleapis.com/css2?family=Italianno&family=Roboto+Condensed:wght@300;400&display=swap">
<style>
  :root {
    --gold: #9c7535;
    --gold-dark: #8a6428;
    --text: #2f2f2f;
    --paper: #fbf8f3;
    --paper-2: #f3eee6;
  }
  html, body { margin: 0; padding: 0; overflow: hidden; }
  body { width: 1200px; height: 1200px; }
  .flyer {
    position: relative;
    width: 1200px; height: 1200px; overflow: hidden;
    background: linear-gradient(160deg, var(--paper) 0%, #fff 40%, var(--paper-2) 100%);
    font-family: "Roboto Condensed", "Arial Narrow", sans-serif;
    font-weight: 300;
    color: var(--text);
  }
  .bottom-band { position: absolute; left: 0; top: 940px; width: 1200px; height: 260px; z-index: 0; }
  .content { position: absolute; inset: 0; z-index: 1; }
  .photo { position: absolute; }
  .photo--breakfast {
    left: 0; top: 0; width: 600px; height: 287px;
    background: linear-gradient(135deg, #e8d6bf 0%, #f3e3c8 35%, #f2b66a 60%, #d8472e 85%, #c7a27a 100%);
  }
  .script {
    font-family: "Italianno", cursive;
    font-weight: 400;
    color: var(--gold);
    margin: 0;
    line-height: 1;
  }
  .heading { position: absolute; font-size: 46px; }
  .body-text {
    position: absolute; margin: 0;
    font-size: 18.5px; line-height: 28px;
  }
  .accommodation-title { left: 655px; top: 52px; font-size: 50px; }
  .accommodation-text { left: 660px; top: 122px; width: 470px; line-height: 24px; }

  .tile { position: absolute; width: 215px; height: 143px; margin: 0; }
  .tile__img { width: 100%; height: 100%; }
  .tile__caption {
    position: absolute; left: 0; top: 118px;
    font-size: 44px; white-space: nowrap;
  }
  .tile--lounge { left: 660px; top: 247px; }
  .tile--lounge .tile__img { background: linear-gradient(135deg, #7da060 0%, #efe4d4 40%, #b8362c 70%, #4a403c 100%); }
  .tile--reception { left: 922px; top: 247px; }
  .tile--reception .tile__img { background: linear-gradient(135deg, #a9b4c0 0%, #f4eee4 40%, #a8303a 70%, #e8dccb 100%); }
  .tile--buffet { left: 660px; top: 447px; }
  .tile--buffet .tile__img { background: linear-gradient(135deg, #d9d9d9 0%, #8a4a22 40%, #c06a2a 65%, #e6ccb0 100%); }
  .tile--entrance { left: 922px; top: 447px; }
  .tile--entrance .tile__img { background: linear-gradient(135deg, #2d3f66 0%, #3d5a8c 40%, #e7c77a 60%, #b32432 100%); }

  .comfort-title { left: 78px; top: 322px; }
  .comfort-title span { display: block; }
  .comfort-title .line-2 { padding-left: 70px; margin-top: 2px; }
  .comfort-text { left: 76px; top: 438px; width: 460px; }

  .rest-title { left: 78px; top: 676px; }
  .rest-title span { display: block; }
  .rest-title .line-2 { padding-left: 208px; margin-top: -8px; }
  .rest-text { left: 76px; top: 784px; width: 460px; }

  .amenities-title { left: 652px; top: 662px; font-size: 46px; }
  .amenities {
    position: absolute; top: 730px; margin: 0; padding: 0; list-style: none;
    font-size: 17.5px;
  }
  .amenities li { position: relative; height: 34px; line-height: 24px; padding-left: 29px; }
  .amenities li svg { position: absolute; left: 0; top: 6px; width: 14px; height: 12px; }
  .amenities--left { left: 659px; }
  .amenities--right { left: 921px; }
</style>
</head>
<body>
<div class="flyer">
  <svg class="bottom-band" viewBox="0 940 1200 260" preserveAspectRatio="none">
    <defs>
      <linearGradient id="room-left" x1="0" y1="0" x2="1" y2="1">
        <stop offset="0" stop-color="#e9e4dc"/><stop offset="0.6" stop-color="#cfcac4"/><stop offset="1" stop-color="#f2efe9"/>
      </linearGradient>
      <linearGradient id="room-middle" x1="0" y1="0" x2="1" y2="1">
        <stop offset="0" stop-color="#9fb1c4"/><stop offset="0.5" stop-color="#f0e8dc"/><stop offset="0.75" stop-color="#a8303a"/><stop offset="1" stop-color="#efe6d6"/>
      </linearGradient>
      <linearGradient id="room-right" x1="0" y1="0" x2="1" y2="1">
        <stop offset="0" stop-color="#f6eeee"/><stop offset="0.5" stop-color="#f3e6e4"/><stop offset="1" stop-color="#d2505a"/>
      </linearGradient>
      <clipPath id="below-wave">
        <path d="M0 1046 C150 991 300 958 450 962 C640 968 760 1094 905 1089 C1020 1085 1120 1038 1200 1022 L1200 1200 L0 1200 Z"/>
      </clipPath>
    </defs>
    <g clip-path="url(#below-wave)">
      <rect x="0" y="950" width="407" height="250" fill="url(#room-left)" role="img" aria-label="Foto: Einzelzimmer mit Leselampe"/>
      <rect x="407" y="950" width="406" height="250" fill="url(#room-middle)" role="img" aria-label="Foto: Flur mit Treppe und Rezeption"/>
      <rect x="813" y="950" width="387" height="250" fill="url(#room-right)" role="img" aria-label="Foto: Familienzimmer unter dem Dach"/>
    </g>
    <path d="M0 1046 C150 991 300 958 450 962 C640 968 760 1094 905 1089 C1020 1085 1120 1038 1200 1022" fill="none" stroke="#9c7535" stroke-width="12"/>
  </svg>

  <div class="content">
    <div class="photo photo--breakfast" role="img" aria-label="Foto: Frühstücksbuffet mit Eiern, Aufschnitt, Tomate-Mozzarella und Obst im Frühstücksraum"></div>

    <h2 class="script heading accommodation-title">Unterkunft:</h2>
    <p class="body-text accommodation-text">Nach einem reichhaltigen Frühstück starten Sie gut gestärkt in den Tag. Genau richtig, um einen Ausflug in die Umgebung zu unternehmen.</p>

    <figure class="tile tile--lounge">
      <div class="tile__img" role="img" aria-label="Foto: Lounge-Bereich mit Sesseln"></div>
      <figcaption class="script tile__caption">Lounge-Bereich</figcaption>
    </figure>
    <figure class="tile tile--reception">
      <div class="tile__img" role="img" aria-label="Foto: Rezeption mit Treppe"></div>
      <figcaption class="script tile__caption">Rezeption</figcaption>
    </figure>
    <figure class="tile tile--buffet">
      <div class="tile__img" role="img" aria-label="Foto: Marmeladen am Frühstücksbuffet"></div>
      <figcaption class="script tile__caption">Frühstücksbuffet</figcaption>
    </figure>
    <figure class="tile tile--entrance">
      <div class="tile__img" role="img" aria-label="Foto: beleuchteter Hoteleingang bei Nacht"></div>
      <figcaption class="script tile__caption">Eingangsbereich</figcaption>
    </figure>

    <h1 class="script heading comfort-title">
      <span class="line-1">Komfort und Tradition:</span>
      <span class="line-2">Lindauer Hotel Garni in Vechta</span>
    </h1>
    <p class="body-text comfort-text">Als ruhiges Familien- und Nichtraucherhotel ist es bei seinen Gästen hoch geschätzt. Helle, freundlich gestaltete Zimmer und ein Service, der keine Wünsche offen lässt. Keine Frage, wer einen Aufenthalt in der altehrwürdigen Stadt Vechta plant, der wird sich von diesem Hotel begeistern können! Zentral gelegen bietet Lindauer Hotel in Vechta die ideale Ausgangsposition für Ausflüge in die nähere Umgebung.</p>

    <h2 class="script heading rest-title">
      <span class="line-1">Finden Sie Ruhe und</span>
      <span class="line-2">Erholung im Schlaf!</span>
    </h2>
    <p class="body-text rest-text">Vechta bietet Geschäfts- und Erholungsreisenden eine Vielzahl an Möglichkeiten. Die dafür nötige Ruhe tanken Sie in Lindauer Hotel. Modern eingerichtete Einzel-, Doppel-, Dreibett-, Familienzimmer und Apartments mit Küche – allesamt mit Dusche/WC und kostenfreiem Zugang ins Internet (WLAN) und Stella TV.</p>

    <h2 class="script heading amenities-title">weitere Annehmlichkeiten:</h2>
    <ul class="amenities amenities--left">
      <li><svg viewBox="0 0 14 12"><path d="M1 6.5 L5 10.5 L13 1" fill="none" stroke="#9c7535" stroke-width="2.6"/></svg>kostenfreies WLAN</li>
      <li><svg viewBox="0 0 14 12"><path d="M1 6.5 L5 10.5 L13 1" fill="none" stroke="#9c7535" stroke-width="2.6"/></svg>Private Parkplätze (4€ pro Tag)</li>
      <li><svg viewBox="0 0 14 12"><path d="M1 6.5 L5 10.5 L13 1" fill="none" stroke="#9c7535" stroke-width="2.6"/></svg>Haustiere sind nicht gestattet</li>
      <li><svg viewBox="0 0 14 12"><path d="M1 6.5 L5 10.5 L13 1" fill="none" stroke="#9c7535" stroke-width="2.6"/></svg>Minimarkt vor Ort</li>
      <li><svg viewBox="0 0 14 12"><path d="M1 6.5 L5 10.5 L13 1" fill="none" stroke="#9c7535" stroke-width="2.6"/></svg>Snackautomat, Getränkeautomat</li>
      <li><svg viewBox="0 0 14 12"><path d="M1 6.5 L5 10.5 L13 1" fill="none" stroke="#9c7535" stroke-width="2.6"/></svg>Nichtraucherzimmer</li>
      <li><svg viewBox="0 0 14 12"><path d="M1 6.5 L5 10.5 L13 1" fill="none" stroke="#9c7535" stroke-width="2.6"/></svg>Aufzug</li>
      <li><svg viewBox="0 0 14 12"><path d="M1 6.5 L5 10.5 L13 1" fill="none" stroke="#9c7535" stroke-width="2.6"/></svg>Heizung</li>
    </ul>
    <ul class="amenities amenities--right">
      <li><svg viewBox="0 0 14 12"><path d="M1 6.5 L5 10.5 L13 1" fill="none" stroke="#9c7535" stroke-width="2.6"/></svg>Fahrradverleih</li>
      <li><svg viewBox="0 0 14 12"><path d="M1 6.5 L5 10.5 L13 1" fill="none" stroke="#9c7535" stroke-width="2.6"/></svg>Golfplatz (max. 3 km entfernt)</li>
      <li><svg viewBox="0 0 14 12"><path d="M1 6.5 L5 10.5 L13 1" fill="none" stroke="#9c7535" stroke-width="2.6"/></svg>Wandern</li>
      <li><svg viewBox="0 0 14 12"><path d="M1 6.5 L5 10.5 L13 1" fill="none" stroke="#9c7535" stroke-width="2.6"/></svg>Radfahren</li>
      <li><svg viewBox="0 0 14 12"><path d="M1 6.5 L5 10.5 L13 1" fill="none" stroke="#9c7535" stroke-width="2.6"/></svg>Express-Check-in/-out</li>
      <li><svg viewBox="0 0 14 12"><path d="M1 6.5 L5 10.5 L13 1" fill="none" stroke="#9c7535" stroke-width="2.6"/></svg>Safe</li>
      <li><svg viewBox="0 0 14 12"><path d="M1 6.5 L5 10.5 L13 1" fill="none" stroke="#9c7535" stroke-width="2.6"/></svg>Zeitungen</li>
      <li><svg viewBox="0 0 14 12"><path d="M1 6.5 L5 10.5 L13 1" fill="none" stroke="#9c7535" stroke-width="2.6"/></svg>Schuhputzmaschine</li>
      <li>-service</li>
    </ul>
  </div>
</div>
</body>
</html>
```